Business Card Design Project

Company name will be Tolvan Crest (named after my black lab and his fraying muzzle) Business is in the body armor, Security product industry servicing the state, local, and federal law enforcement markets. I want a more formal and serious logo for both business cards and letterhead

```html
<!DOCTYPE html>
<html lang="en">
<head>
<meta charset="utf-8">
<title>Tolvan Crest – Business Card</title>
<link rel="stylesheet" href="https://fonts.googleapis.com/css2?family=Open+Sans:wght@400;600;700&display=swap">
<style>
  :root {
    --backdrop: #3a2a20;
    --card: #ffffff;
    --frame: #5a5a5c;
    --ink: #1d1d1f;
    --ink-soft: #444446;
    --rule: #6a6a6c;
  }
  * { margin: 0; padding: 0; box-sizing: border-box; }
  html, body {
    width: 1200px;
    height: 900px;
    overflow: hidden;
    background: var(--backdrop);
  }
  body {
    position: relative;
    font-family: "Open Sans", sans-serif;
  }
  .card {
    position: absolute;
    left: 80px;
    top: 157px;
    width: 1040px;
    height: 585px;
    background: var(--card);
  }
  .card-frame {
    position: absolute;
    inset: 8px;
    border: 12px solid var(--frame);
  }
  .brand {
    position: absolute;
    left: 60px;
    width: 392px;
    top: 262px;
    text-align: center;
    font-size: 44px;
    font-weight: 700;
    letter-spacing: 1px;
    color: var(--ink);
    line-height: 1;
  }
  .divider {
    position: absolute;
    left: 499px;
    top: 110px;
    width: 2px;
    height: 364px;
    background: var(--rule);
  }
  .person {
    position: absolute;
    left: 566px;
    top: 112px;
  }
  .person-name {
    font-size: 37px;
    font-weight: 700;
    color: var(--ink);
    line-height: 1.2;
  }
  .person-title {
    font-size: 25px;
    font-weight: 400;
    color: var(--ink-soft);
    margin-top: 2px;
  }
  .contact-list {
    position: absolute;
    left: 566px;
    top: 286px;
    list-style: none;
  }
  .contact-item {
    display: flex;
    align-items: flex-start;
    font-size: 25px;
    color: var(--ink-soft);
    line-height: 35px;
    margin-bottom: 17px;
  }
  .contact-icon {
    width: 34px;
    height: 35px;
    flex: none;
    margin-right: 14px;
    fill: var(--ink);
  }
</style>
</head>
<body>
  <div class="card">
    <div class="card-frame"></div>

    <div class="brand">Tolvan Crest</div>

    <div class="divider"></div>

    <div class="person">
      <div class="person-name">Reid Calloway</div>
      <div class="person-title">Manufacturers Rep Principal</div>
    </div>

    <ul class="contact-list">
      <li class="contact-item">
        <svg class="contact-icon" viewBox="0 0 34 35" aria-hidden="true">
          <path d="M8 6 L13 6 L15 13 L11.5 16 C13.5 20.5 16.5 23.5 21 25.5 L24 22 L31 24 L31 29 C31 30.5 30 31 28.5 31 C16 30 5 19 4 7.5 C4 6.5 5 6 6 6 Z"/>
        </svg>
        <span>555-014-2287</span>
      </li>
      <li class="contact-item">
        <svg class="contact-icon" viewBox="0 0 34 35" aria-hidden="true">
          <path d="M3 9 H31 V27 H3 Z M5 11 L17 20 L29 11 V25 H5 Z" fill-rule="evenodd"/>
          <path d="M3 9 L17 19.5 L31 9 Z"/>
        </svg>
        <span>rcalloway@tolvancrest.com</span>
      </li>
      <li class="contact-item">
        <svg class="contact-icon" viewBox="0 0 34 35" aria-hidden="true">
          <path d="M17 5 L32 17 L28.5 17 L17 8 L5.5 17 L2 17 Z"/>
          <path d="M7 18 L17 10.5 L27 18 V31 H20 V24 H14 V31 H7 Z"/>
        </svg>
        <span>1740 Harbor Lane South<br>Marlow Bay, FL 32099</span>
      </li>
    </ul>
  </div>
</body>
</html>
```